Improve the UI for two Mobile Apps

Brevano licenses ERP software to mid-sized companies (50M plus). Brevano's product suite includes procurement, accounting and CRM applications.

We have two mobile Apps that integrate with our ERP applications - Tallyway Hub and Morrow Field Kit. The Tallyway Hub App allows a user to review and approve requisitions, purchase orders, supplier invoices and expense reports which are forwarded to the App from our ERP applications. The expense report App allows a user to enter travel expenses and attach photos of receipts.

We are satisfied with the functionality of both mobile Apps. Our goal is to improve the aesthetics (fonts, colors, graphics). We are looking for a clean, light weight, modern design. The design should also be consistent with our current Brevano colors (blue and green) and branding (see www.brevanosystems.com).

Documentation showing current screen shots for each App is attached (2 files).
Updates

Please focus on the 14 major forms in the attachment. The larger document includes about 40 forms. It is intended to illustrate the use of the Apps which hopefully is useful when considering design alternatives. We realize the budget may be insufficient for the complete redesign of both Apps. When accepting the final design we will negotiate a price for revising / completing all forms. At this point we will increase the project's budget or complete the remaining work in-house. Thanks, Derek...

Target Market(s)

We sell to mid-large sized corporations. Are primary customer is the purchasing agent.

Industry/Entity Type

Accounting

Number of Pages Required

5+ page

Requirements
Must have
• Clean, modern design of the major entry forms shown in the attached documents. I need graphics and colors only. Our developers will adjust the Apps. I have attached 2 sets of documents. The first 2 files illustrate the use of all forms in both apps. Several forms appear multiple times. The second set of 3 files include the unique forms in both apps (14 in total). These files are labeled "(major forms)".

```html
<!DOCTYPE html>
<html lang="en">
<head>
<meta charset="utf-8">
<title>Brevano – Server Registration</title>
<link rel="stylesheet" href="https://fonts.googleapis.com/css2?family=Montserrat:wght@500;800&display=swap">
<style>
  :root {
    --header-bg: #2b2b2b;
    --page-bg: #3c3c3c;
    --brand-blue: #1d8ee0;
    --button-blue: #1a7fcf;
    --button-text: #ffffff;
    --field-bg: #ffffff;
    --field-border: #d9d9d9;
    --placeholder: #9b9b9b;
  }

  * { box-sizing: border-box; margin: 0; padding: 0; }

  html, body {
    width: 1200px;
    height: 933px;
    overflow: hidden;
    background: var(--page-bg);
    font-family: "Montserrat", Arial, sans-serif;
  }

  .app-screen {
    position: relative;
    width: 1200px;
    height: 933px;
    background: var(--page-bg);
  }

  .app-header {
    position: absolute;
    left: 0;
    top: 0;
    width: 1200px;
    height: 183px;
    background: var(--header-bg);
  }

  .brand-name {
    position: absolute;
    left: 329px;
    top: 46px;
    width: 402px;
    text-align: center;
    font-weight: 800;
    font-size: 70px;
    line-height: 76px;
    letter-spacing: 1px;
    color: var(--brand-blue);
    white-space: nowrap;
  }

  .register-banner {
    position: absolute;
    left: 263px;
    top: 231px;
    width: 408px;
    height: 76px;
    border-radius: 11px;
    background: var(--button-blue);
    color: var(--button-text);
    font-weight: 500;
    font-size: 21px;
    white-space: nowrap;
    display: flex;
    align-items: center;
    justify-content: center;
  }

  .registration-form {
    position: absolute;
    left: 217px;
    top: 343px;
    width: 499px;
  }

  .form-field {
    position: absolute;
    left: 0;
    width: 499px;
    height: 72px;
    background: var(--field-bg);
    border: 1px solid var(--field-border);
    display: flex;
    align-items: center;
    padding-left: 31px;
    font-weight: 500;
    font-size: 24px;
    color: var(--placeholder);
    white-space: nowrap;
  }

  .field-username { top: 0; }
  .field-password { top: 93px; }
  .field-server-address { top: 188px; }
  .field-server-application { top: 281px; }
</style>
</head>
<body>
  <main class="app-screen">
    <header class="app-header">
      <div class="brand-name">BREVANO</div>
    </header>

    <div class="register-banner">Please Register with the Server</div>

    <form class="registration-form">
      <div class="form-field field-username">Username</div>
      <div class="form-field field-password">Password</div>
      <div class="form-field field-server-address">Server Address</div>
      <div class="form-field field-server-application">Server Application</div>
    </form>
  </main>
</body>
</html>
```